Association le rameau d'Ostrelle needs a web design design

hello I would like to redo the website of my charity for it to be clearer and more profesional,our association is involved in a orphanage in haiti in port- au-prince here is the first site I did, but it is not very pretty or very credible.

http://arbostrelle.example.org/arbo

Industry/Entity Type

Charity

```html
<!DOCTYPE html>
<html lang="en">
<head>
<meta charset="utf-8">
<title>Ostrelle – Association le rameau d'Ostrelle</title>
<link href="https://fonts.googleapis.com/css2?family=Lato:wght@400;700&family=Open+Sans:wght@400;600;700&display=swap" rel="stylesheet">
<style>
:root{
  --nav-bg:#560a2c;
  --magenta:#c1136f;
  --magenta-dark:#8e0b47;
  --maroon:#650b37;
  --green:#8cc21f;
  --text:#2b2b2b;
  --footer:#e9e9ea;
  --white:#ffffff;
}
*{margin:0;padding:0;box-sizing:border-box}
html,body{width:810px;height:1200px;overflow:hidden;background:var(--white)}
body{position:relative;font-family:'Lato',sans-serif;color:var(--text)}
.abs{position:absolute}
.header-band{left:0;top:0;width:810px;height:430px}
.nav{left:0;top:0;width:810px;height:38px;background:var(--nav-bg)}
.nav-link{top:11px;font-size:11px;color:var(--white);white-space:nowrap}
.nav-link.active{color:var(--green)}
.nav-underline{left:74px;top:37px;width:67px;height:2px;background:var(--green)}
.search{left:565px;top:8px;width:166px;height:21px;border:1px solid #8a1d4c;border-radius:11px;background:#3f0720}
.search span{position:absolute;left:8px;top:4px;font-size:7px;color:#ddd}
.search svg{position:absolute;right:5px;top:3px}
.brand{left:77px;top:58px;font-family:'Open Sans',sans-serif;font-weight:700;font-size:29px;color:var(--white);letter-spacing:-1.5px}
.call{left:403px;top:64px;font-size:18px;color:var(--white);white-space:nowrap}
.call-icon{left:373px;top:63px}
.donate-btn{left:627px;top:61px;width:110px;height:29px;border-radius:7px;background:var(--green);color:var(--white);font-size:13px;text-align:center;line-height:29px}
.hero{left:74px;top:112px;width:660px;height:334px;background:linear-gradient(180deg,#caa067 0%,#f2b24a 45%,#f6a12c 70%,#5a3410 100%)}
.hero-shadow{left:70px;top:442px;width:680px;height:26px;background:radial-gradient(ellipse at 50% 0%,rgba(0,0,0,.45),rgba(0,0,0,0) 70%)}
.dot{top:146px;width:6px;height:6px;border-radius:50%;background:var(--white)}
.dot.on{background:var(--green)}
.welcome-img{left:81px;top:506px;width:416px;height:118px;background:linear-gradient(90deg,#bdbdbd,#4a4a4a 55%,#6f6f6f)}
.welcome-box{left:95px;top:538px;width:186px;height:57px;background:#050505;padding:7px 10px;font-size:12.5px;line-height:15px;color:var(--white)}
.welcome-box strong{font-family:'Open Sans',sans-serif;font-weight:700;color:#a3113f}
.intro{left:82px;top:634px;width:418px;font-size:10.6px;line-height:17.5px;color:var(--text)}
.intro p+p{margin-top:17px}
.news{left:526px;top:506px;width:208px;height:233px;background:var(--green);color:var(--white)}
.news h2{position:absolute;left:9px;top:11px;font-family:'Open Sans',sans-serif;font-weight:600;font-size:17px}
.news-img{left:10px;top:40px;width:188px;height:114px;background:linear-gradient(135deg,#7d6048,#3b3430 60%,#5e78a0)}
.news-date{left:9px;top:166px;font-family:'Open Sans',sans-serif;font-weight:600;font-size:10.5px}
.news-text{left:10px;top:186px;width:180px;font-size:8px;line-height:13px}
.section-title{top:780px;font-family:'Open Sans',sans-serif;font-weight:600;font-size:18px;color:var(--maroon)}
.video{left:74px;top:822px;width:435px;height:224px;border:4px solid var(--maroon);border-bottom-width:5px;background:linear-gradient(135deg,#6b5a48,#2a2320 50%,#3a2a50)}
.play{left:267px;top:908px}
.gallery{left:526px;top:822px;width:207px;height:224px;background:linear-gradient(135deg,#a07a58,#c43a3a 40%,#3a3638 75%)}
.gallery-caption{left:526px;top:994px;width:207px;height:52px;background:var(--maroon);color:var(--white);font-size:11px;line-height:16px;padding:9px 13px}
.arrow{top:911px}
.card-shadow{top:1046px;height:14px;background:radial-gradient(ellipse at 50% 0%,rgba(0,0,0,.18),rgba(0,0,0,0) 70%)}
.footer-band{left:0;top:1060px;width:810px;height:140px}
.social{top:1106px;width:25px;height:25px;border:1.5px solid;border-radius:50%;background:var(--white)}
.footer-links{left:0;top:1144px;width:810px;text-align:center;font-size:8px;color:#333;word-spacing:1px}
.footer-links span{margin:0 11px}
.copyright{left:0;top:1172px;width:810px;text-align:center;font-size:8px;color:#333}
</style>
</head>
<body>
<svg class="abs header-band" width="810" height="430" viewBox="0 0 810 430" aria-hidden="true">
  <defs>
    <linearGradient id="bandGrad" x1="0" y1="0" x2="0" y2="1">
      <stop offset="0" stop-color="#c1136f"/>
      <stop offset="1" stop-color="#8e0b47"/>
    </linearGradient>
  </defs>
  <polygon points="0,0 810,0 810,282 0,420" fill="url(#bandGrad)"/>
</svg>

<nav class="abs nav">
  <span class="abs nav-link active" style="left:97px">Home</span>
  <span class="abs nav-link" style="left:157px">The Association</span>
  <span class="abs nav-link" style="left:259px">The Orphanage</span>
  <span class="abs nav-link" style="left:360px">News</span>
  <span class="abs nav-link" style="left:416px">Donations</span>
  <span class="abs nav-link" style="left:493px">Contact Us</span>
  <div class="abs nav-underline"></div>
  <div class="abs search"><span>Search</span>
    <svg width="13" height="13" viewBox="0 0 13 13"><circle cx="5.5" cy="5.5" r="4" fill="none" stroke="#fff" stroke-width="1.5"/><line x1="8.5" y1="8.5" x2="12" y2="12" stroke="#fff" stroke-width="1.8"/></svg>
  </div>
</nav>

<div class="abs brand">Ostrelle</div>
<svg class="abs call-icon" width="26" height="26" viewBox="0 0 26 26" aria-hidden="true">
  <circle cx="13" cy="13" r="11.5" fill="none" stroke="#8cc21f" stroke-width="1.6"/>
  <path d="M9 7c1 0 2 2.5 2 3s-1 1-1 1.5 2 3.5 3.5 4 1-1 1.5-1 3 1 3 2-1.5 2-2.5 2C11 18.5 7.5 14 7.5 10 7.5 8.5 8 7 9 7z" fill="#8cc21f"/>
</svg>
<div class="abs call">Call Now : 1-800-555-0147</div>
<div class="abs donate-btn">Make Donation</div>

<div class="abs hero-shadow"></div>
<div class="abs hero" role="img" aria-label="Children silhouetted running through a meadow at sunset"></div>
<div class="abs dot on" style="left:381px"></div>
<div class="abs dot" style="left:391px"></div>
<div class="abs dot" style="left:402px"></div>
<div class="abs dot" style="left:412px"></div>
<div class="abs dot" style="left:423px"></div>

<div class="abs welcome-img" role="img" aria-label="Black and white photo of smiling orphanage children"></div>
<div class="abs welcome-box">Welcome to the website of<br><strong>the association Bough orphanage in Haiti</strong></div>
<div class="abs intro">
  <p>L'association ARBO est une structure non lucrative établie à Genève, afin de soutenir l' Orphelinat le Rameau à Haïti.créé au lendemain du séisme du 12 janvier 2010.</p>
  <p>L'orphelinat et l'association souhaitent apporter leur aide à une partie des quelques 100 000 enfants orphelins que compte Haïti suite à cette catastrophe.</p>
</div>

<aside class="abs news">
  <h2>News</h2>
  <div class="abs news-img" role="img" aria-label="Event room decorated with balloons"></div>
  <div class="abs news-date">March 23,2015 at 19:00</div>
  <div class="abs news-text">Our first event organized in support of the association will be held</div>
</aside>

<h2 class="abs section-title" style="left:74px">Featured Videos</h2>
<h2 class="abs section-title" style="left:525px">Photo Gallery</h2>

<div class="abs card-shadow" style="left:90px;width:420px"></div>
<div class="abs card-shadow" style="left:530px;width:200px"></div>

<div class="abs video" role="img" aria-label="Video still of a fundraising evening with balloons and guests"></div>
<svg class="abs play" width="50" height="50" viewBox="0 0 50 50" aria-hidden="true">
  <circle cx="25" cy="25" r="23" fill="#2a2a2a" stroke="#d8d8d8" stroke-width="2.5"/>
  <polygon points="19,14 36,25 19,36" fill="#fff"/>
</svg>

<div class="abs gallery" role="img" aria-label="Gallery photo of a guest holding red balloons"></div>
<svg class="abs arrow" style="left:533px" width="12" height="16" viewBox="0 0 12 16" aria-hidden="true"><polyline points="9,2 3,8 9,14" fill="none" stroke="#fff" stroke-width="2"/></svg>
<svg class="abs arrow" style="left:704px" width="12" height="16" viewBox="0 0 12 16" aria-hidden="true"><polyline points="3,2 9,8 3,14" fill="none" stroke="#fff" stroke-width="2"/></svg>
<div class="abs gallery-caption">Neque porro quisquam est qui dolorem ipsum quia dolor sit amet</div>

<svg class="abs footer-band" width="810" height="140" viewBox="0 0 810 140" aria-hidden="true">
  <polygon points="0,46 810,8 810,140 0,140" fill="#e9e9ea"/>
</svg>
<footer>
  <div class="abs social" style="left:333px;border-color:#3a8fd0"></div>
  <div class="abs social" style="left:362px;border-color:#3b5a98"></div>
  <div class="abs social" style="left:391px;border-color:#d2433a"></div>
  <div class="abs social" style="left:420px;border-color:#1f78b4"></div>
  <div class="abs social" style="left:452px;border-color:#c6292b"></div>
  <div class="abs footer-links">Home<span>|</span>The Association<span>|</span>The Orphanage<span>|</span>News<span>|</span>Donations<span>|</span>Contact Us</div>
  <div class="abs copyright">© 2014 Company Name,All Rights Reserved</div>
</footer>
</body>
</html>
```